Fernvale Business Card Design

We are looking for a fresh business card design for our new logo. We would like a business card that is unique but friendly. We are in the window coverings business offering blinds, shutters and shades for homes.

Target Market(s)

Targeting the end-consumer

Industry/Entity Type

Business

Requirements
Must have
• Must have a dedicates space for a photo of our sales person. Must contain our new logo (attached).

```html
<!DOCTYPE html>
<html lang="en">
<head>
<meta charset="utf-8">
<title>Fernvale Business Card</title>
<link rel="stylesheet" href="https://fonts.googleapis.com/css2?family=Open+Sans:wght@400;600;700&display=swap">
<style>
  :root {
    --page-bg: #e6e7e8;
    --card-bg: #ffffff;
    --card-edge: #d4d6d8;
    --ink: #3c3d3f;
    --ink-soft: #4a4b4d;
    --brand-green: #6aa832;
    --photo-light: #b8977a;
    --photo-mid: #7a5c45;
    --photo-dark: #2a2523;
  }
  * { margin: 0; padding: 0; box-sizing: border-box; }
  html, body {
    width: 1200px; height: 970px; overflow: hidden;
    background: var(--page-bg);
    font-family: "Open Sans", sans-serif;
  }
  .card {
    position: absolute; left: 100px; top: 207px;
    width: 1000px; height: 556px;
    background: var(--card-bg);
    border: 1px solid var(--card-edge);
    overflow: hidden;
  }
  .brand {
    position: absolute; left: 49px; top: 45px;
    display: flex; align-items: center; gap: 26px;
  }
  .brand-square {
    width: 100px; height: 100px;
    background: var(--brand-green);
  }
  .brand-name {
    font-size: 66px; font-weight: 400; color: var(--ink-soft);
    letter-spacing: 0.5px; line-height: 1;
  }
  .person { position: absolute; left: 49px; top: 214px; }
  .person-name {
    font-size: 29px; font-weight: 700; color: var(--brand-green);
    letter-spacing: 0.5px; line-height: 1.2;
  }
  .person-role { font-size: 23px; color: var(--ink); line-height: 1.3; }
  .address {
    position: absolute; left: 49px; top: 302px;
    font-size: 23px; color: var(--ink); line-height: 31px;
  }
  .contacts {
    position: absolute; left: 49px; top: 383px;
    list-style: none; font-size: 23px; color: var(--ink);
  }
  .contacts li {
    display: flex; align-items: center; gap: 10px; height: 33.5px;
  }
  .contacts svg { width: 22px; height: 22px; fill: var(--brand-green); flex: none; }
  .portrait {
    position: absolute; left: 560px; top: 40px; right: 0; bottom: 0;
    background:
      radial-gradient(ellipse 30% 32% at 52% 38%, var(--photo-light), transparent 70%),
      linear-gradient(180deg, var(--photo-mid) 0%, var(--photo-mid) 60%, var(--photo-dark) 100%);
    border-radius: 200px 200px 0 0;
  }
</style>
</head>
<body>
  <div class="card">
    <div class="brand">
      <div class="brand-square"></div>
      <span class="brand-name">Fernvale</span>
    </div>

    <div class="person">
      <p class="person-name">MAREN HOLLOWAY</p>
      <p class="person-role">Managing Director</p>
    </div>

    <p class="address">Level 12, 5 Larkspur Tower<br>Sydney, 20, New South Wales</p>

    <ul class="contacts">
      <li>
        <svg viewBox="0 0 24 24" aria-hidden="true"><path d="M7 1h10a2 2 0 0 1 2 2v18a2 2 0 0 1-2 2H7a2 2 0 0 1-2-2V3a2 2 0 0 1 2-2zm0 3v13h10V4zm5 15a1.3 1.3 0 1 0 0 2.6A1.3 1.3 0 0 0 12 19z"/></svg>
        + 000 000 0000
      </li>
      <li>
        <svg viewBox="0 0 24 24" aria-hidden="true"><path d="M2 9c0-3 5-5 10-5s10 2 10 5v2h-5V8.5c-3-1-7-1-10 0V11H2zm4 3h12l3 8H3zm6 1.5a3 3 0 1 0 0 6 3 3 0 0 0 0-6z"/></svg>
        + 000 000 0000
      </li>
      <li>
        <svg viewBox="0 0 24 24" aria-hidden="true"><path d="M2 5h20v14H2zm2 2v.5l8 5.5 8-5.5V7zm0 2.9V17h16V9.9l-8 5.5z"/></svg>
        Maren@fernvale.com
      </li>
      <li>
        <svg viewBox="0 0 24 24" aria-hidden="true"><path d="M12 2a10 10 0 1 1 0 20 10 10 0 0 1 0-20zm0 2a8 8 0 0 0-7.4 5h5l1 2-2 2 1 4 1 1v2.9A8 8 0 0 0 12 20a8 8 0 0 0 7.7-6h-3.7l-2-2 1-3 3-2A8 8 0 0 0 12 4z"/></svg>
        www.fernvale.com
      </li>
    </ul>

    <div class="portrait" role="img" aria-label="Portrait photo of the sales person"></div>
  </div>
</body>
</html>
```